Springtime Flyer Design

We are looking to redesign our flyer that we distribute to approximately 70,000 homes every spring. We would like it to emulate the other designs we recently had done on ArtFlockz which we have attached with a copy of our existing flyer. Thank you for looking at this project!

Target Market(s)

Residential homeowners

Industry/Entity Type

Landscaping

Font styles to use
Serif
Sans Serif

Requirements
Must have
• 1. Remove the TK Haulage logo on the bottom right
• 2. It should include all of the services offered but maybe in a nicer way
• 3. Should have our email and phone number on the flyer
• 4.Looking for a totally updated design that looks more contemporary and has a similar look to the attached files that we had done earlier on ArtFlock.
• 5. This flyer is printed on white or yellow paper.
Nice to have
• Completely updated design

```html
<!DOCTYPE html>
<html lang="en">
<head>
<meta charset="utf-8">
<title>Willow Brook Landscaping – Spring Flyer</title>
<link href="https://fonts.googleapis.com/css2?family=Cinzel:wght@400;500&family=Lato:wght@400;700&display=swap" rel="stylesheet">
<style>
  :root {
    --ink: #1c1c1e;
    --white: #ffffff;
    --green: #3aaa5c;
    --green-bright: #3cb55a;
    --blue: #4a9ad6;
    --text: #e8e8e8;
  }
  * { margin: 0; padding: 0; box-sizing: border-box; }
  html, body { width: 923px; height: 1200px; overflow: hidden; background: var(--ink); }
  .flyer { position: relative; width: 923px; height: 1200px; background: var(--ink); font-family: "Lato", sans-serif; color: var(--text); }
  .hero { position: absolute; left: 0; top: 0; width: 923px; height: 440px; }
  .brand { position: absolute; top: 480px; left: 0; width: 100%; text-align: center; font-family: "Lato", sans-serif; font-weight: 400; font-size: 38px; line-height: 44px; color: var(--white); }
  .services-line { position: absolute; top: 574px; width: 100%; text-align: center; font-family: "Cinzel", serif; font-size: 31px; color: var(--green); letter-spacing: 1px; }
  .offer-box { position: absolute; left: 69px; top: 663px; width: 774px; height: 258px; border: 1.5px solid var(--white); border-radius: 8px; }
  .offer-title { position: absolute; top: -16px; left: 50%; transform: translateX(-50%); background: var(--ink); padding: 0 32px; font-size: 23px; font-weight: 400; color: var(--blue); letter-spacing: 1px; white-space: nowrap; }
  .service-list { position: absolute; top: 53px; list-style: none; }
  .service-list.left { left: 27px; }
  .service-list.right { left: 430px; }
  .service-list li { display: flex; align-items: center; height: 35px; font-size: 19px; color: var(--white); }
  .service-list svg { width: 16px; height: 16px; margin-right: 12px; flex: none; }
  .badge-offer { position: absolute; left: 765px; top: 671px; width: 134px; height: 134px; }
  .about { position: absolute; left: 50px; top: 951px; width: 826px; font-size: 16px; line-height: 24px; color: var(--text); text-align: center; }
  .memberships { position: absolute; left: 721px; top: 1036px; display: flex; gap: 8px; }
  .memberships span { width: 38px; height: 40px; display: block; }
  .cta { position: absolute; left: 178px; top: 1088px; width: 566px; height: 38px; background: var(--green); border: 2px solid var(--white); border-radius: 10px; color: var(--white); font-size: 24px; text-align: center; line-height: 34px; letter-spacing: 1px; }
  .contact { position: absolute; top: 1145px; left: 22px; right: 22px; display: flex; justify-content: space-between; font-size: 16px; color: var(--white); }
  .contact span { display: flex; align-items: center; gap: 8px; }
  .contact svg { width: 22px; height: 22px; }
</style>
</head>
<body>
<main class="flyer">
  <svg class="hero" viewBox="0 0 923 440">
    <defs>
      <linearGradient id="gardenTone" x1="0" y1="0" x2="0" y2="1">
        <stop offset="0" stop-color="#5f6a4a"/>
        <stop offset="0.45" stop-color="#6f8f3a"/>
        <stop offset="1" stop-color="#86b83a"/>
      </linearGradient>
      <radialGradient id="bedTone" cx="0.5" cy="0.5" r="0.6">
        <stop offset="0" stop-color="#7fae46"/>
        <stop offset="1" stop-color="#3f6b2c"/>
      </radialGradient>
    </defs>
    <path class="wave-stripe" fill="var(--blue)" d="M0,291 C80,330 200,360 330,350 C450,340 600,310 700,315 C800,320 870,370 923,400 V418 C870,388 800,336 700,331 C600,326 450,356 330,366 C200,376 80,346 0,307 Z"/>
    <path role="img" aria-label="Photo of a landscaped front yard with flower beds and lawn" fill="url(#gardenTone)" d="M0,0 H923 V400 C870,370 800,320 700,315 C600,310 450,340 330,350 C200,360 80,330 0,291 Z"/>
    <g class="project-thumbs">
      <circle cx="165" cy="335" r="89" fill="var(--ink)" stroke="var(--white)" stroke-width="2"/>
      <circle cx="165" cy="335" r="78" fill="url(#bedTone)" stroke="var(--white)" stroke-width="3" role="img" aria-label="Photo of a curved stone retaining wall garden bed"/>
      <circle cx="460" cy="333" r="89" fill="var(--ink)" stroke="var(--white)" stroke-width="2"/>
      <circle cx="460" cy="333" r="78" fill="url(#bedTone)" stroke="var(--white)" stroke-width="3" role="img" aria-label="Photo of a home entrance with planted beds"/>
      <circle cx="756" cy="335" r="89" fill="var(--ink)" stroke="var(--white)" stroke-width="2"/>
      <circle cx="756" cy="335" r="78" fill="url(#bedTone)" stroke="var(--white)" stroke-width="3" role="img" aria-label="Photo of a garden path winding through shrubs"/>
    </g>
  </svg>

  <header class="brand">Willow Brook Landscaping</header>

  <p class="services-line">LANDSCAPING • LAWN CARE • LEAF CLEAN-UP</p>

  <section class="offer-box">
    <h2 class="offer-title">ATTENTION – HOMEOWNERS</h2>
    <ul class="service-list left">
      <li><svg viewBox="0 0 16 16"><circle cx="8" cy="8" r="6.5" fill="none" stroke="var(--blue)" stroke-width="1.5"/><path d="M5 8.2 7.2 10.3 11 6" fill="none" stroke="var(--blue)" stroke-width="1.5"/></svg>Weekly lawn maintenance</li>
      <li><svg viewBox="0 0 16 16"><circle cx="8" cy="8" r="6.5" fill="none" stroke="var(--blue)" stroke-width="1.5"/><path d="M5 8.2 7.2 10.3 11 6" fill="none" stroke="var(--blue)" stroke-width="1.5"/></svg>Spring / fall leaf clean-ups</li>
      <li><svg viewBox="0 0 16 16"><circle cx="8" cy="8" r="6.5" fill="none" stroke="var(--blue)" stroke-width="1.5"/><path d="M5 8.2 7.2 10.3 11 6" fill="none" stroke="var(--blue)" stroke-width="1.5"/></svg>Landscaping design and installation</li>
      <li><svg viewBox="0 0 16 16"><circle cx="8" cy="8" r="6.5" fill="none" stroke="var(--blue)" stroke-width="1.5"/><path d="M5 8.2 7.2 10.3 11 6" fill="none" stroke="var(--blue)" stroke-width="1.5"/></svg>Lawn fertilization and weed control</li>
      <li><svg viewBox="0 0 16 16"><circle cx="8" cy="8" r="6.5" fill="none" stroke="var(--blue)" stroke-width="1.5"/><path d="M5 8.2 7.2 10.3 11 6" fill="none" stroke="var(--blue)" stroke-width="1.5"/></svg>Shrub trimming</li>
    </ul>
    <ul class="service-list right">
      <li><svg viewBox="0 0 16 16"><circle cx="8" cy="8" r="6.5" fill="none" stroke="var(--blue)" stroke-width="1.5"/><path d="M5 8.2 7.2 10.3 11 6" fill="none" stroke="var(--blue)" stroke-width="1.5"/></svg>Mulch / bark installation</li>
      <li><svg viewBox="0 0 16 16"><circle cx="8" cy="8" r="6.5" fill="none" stroke="var(--blue)" stroke-width="1.5"/><path d="M5 8.2 7.2 10.3 11 6" fill="none" stroke="var(--blue)" stroke-width="1.5"/></svg>Tree pruning or removal</li>
      <li><svg viewBox="0 0 16 16"><circle cx="8" cy="8" r="6.5" fill="none" stroke="var(--blue)" stroke-width="1.5"/><path d="M5 8.2 7.2 10.3 11 6" fill="none" stroke="var(--blue)" stroke-width="1.5"/></svg>Sod, hydro-seeding</li>
      <li><svg viewBox="0 0 16 16"><circle cx="8" cy="8" r="6.5" fill="none" stroke="var(--blue)" stroke-width="1.5"/><path d="M5 8.2 7.2 10.3 11 6" fill="none" stroke="var(--blue)" stroke-width="1.5"/></svg>Lawn renovation</li>
      <li><svg viewBox="0 0 16 16"><circle cx="8" cy="8" r="6.5" fill="none" stroke="var(--blue)" stroke-width="1.5"/><path d="M5 8.2 7.2 10.3 11 6" fill="none" stroke="var(--blue)" stroke-width="1.5"/></svg>Irrigation installation and service</li>
    </ul>
  </section>

  <svg class="badge-offer" viewBox="0 0 134 134">
    <polygon fill="var(--green-bright)" points="67,0 73,9 81,2 85,12 95,7 96,18 107,16 105,27 116,28 111,38 122,42 114,50 124,57 115,63 124,70 114,76 121,85 110,88 115,98 104,98 106,109 95,107 94,118 84,114 80,124 72,117 67,126 61,117 54,124 50,114 40,118 39,107 28,109 30,98 19,98 24,88 13,85 20,76 10,70 19,63 10,57 20,50 12,42 23,38 18,28 29,27 27,16 38,18 39,7 49,12 53,2 61,9"/>
    <circle cx="67" cy="63" r="50" fill="none" stroke="var(--white)" stroke-width="1.5" stroke-dasharray="2 3"/>
    <text x="67" y="64" text-anchor="middle" font-family="Lato, sans-serif" font-weight="700" fill="var(--white)"><tspan font-size="28">5%</tspan><tspan font-size="18" dx="3">OFF</tspan></text>
    <text x="67" y="81" text-anchor="middle" font-family="Lato, sans-serif" font-weight="700" font-size="9" fill="var(--white)">NEW CUSTOMERS</text>
    <text x="67" y="93" text-anchor="middle" font-family="Lato, sans-serif" font-weight="700" font-size="9" fill="var(--white)">ONLY</text>
  </svg>

  <p class="about">Willow Brook Landscaping has proudly served North East Cedar Falls and surrounding suburbs since 2005. Our commitment and dedication to quality has earned us a reputation we are proud of. Our goal is to exceed your expectations. We look forward to working with you on your next project. Contact us today to get started!</p>

  <div class="memberships" aria-label="Service awards">
    <span><svg viewBox="0 0 38 40"><path d="M3 3 H35 V24 Q35 34 19 39 Q3 34 3 24 Z" fill="#c9a93b"/></svg></span>
    <span><svg viewBox="0 0 38 40"><circle cx="19" cy="17" r="15" fill="#c9a93b"/><path d="M12 29 9 39 16 36 19 30 Z M26 29 29 39 22 36 19 30 Z" fill="var(--green)"/></svg></span>
    <span><svg viewBox="0 0 38 40"><path d="M2 8 Q19 0 36 8 V22 Q36 34 19 39 Q2 34 2 22 Z" fill="#c9a93b"/></svg></span>
    <span><svg viewBox="0 0 38 40"><path d="M3 6 Q19 0 35 6 V22 Q35 34 19 39 Q3 34 3 22 Z" fill="var(--green)" stroke="var(--white)" stroke-width="1.5"/></svg></span>
  </div>

  <div class="cta">Call 555.014.2287 today for a proposal</div>

  <footer class="contact">
    <span><svg viewBox="0 0 22 22"><circle cx="11" cy="11" r="10" fill="var(--green)"/><rect x="5.5" y="7" width="11" height="8" fill="none" stroke="var(--white)" stroke-width="1.4"/><path d="M5.5 7 11 11.5 16.5 7" fill="none" stroke="var(--white)" stroke-width="1.4"/></svg>hello@willowbrookyard.com</span>
    <span><svg viewBox="0 0 22 22"><circle cx="11" cy="11" r="10" fill="var(--green)"/><path d="M11 5a4 4 0 0 1 4 4c0 3-4 8-4 8s-4-5-4-8a4 4 0 0 1 4-4z" fill="none" stroke="var(--white)" stroke-width="1.4"/><circle cx="11" cy="9" r="1.4" fill="var(--white)"/></svg>742 Maple Ridge Road, Cedar Falls, MI 49000</span>
    <span><svg viewBox="0 0 22 22"><circle cx="11" cy="11" r="10" fill="var(--green)"/><circle cx="11" cy="11" r="6" fill="none" stroke="var(--white)" stroke-width="1.3"/><ellipse cx="11" cy="11" rx="2.6" ry="6" fill="none" stroke="var(--white)" stroke-width="1.1"/><path d="M5 11H17" stroke="var(--white)" stroke-width="1.1"/></svg>www.willowbrookyard.com</span>
  </footer>
</main>
</body>
</html>
```